WP website design (Brantow)

We need a wordpress design for an established auction and real estate company based in Kentucky. The winning design will incorporate a professional color scheme with company logo in a clean layout with specified widgets. The design needs to consider that this will be developed on a responsive theme. Colors will complement the colors in the logo.

Industry/Entity Type

Real Estate

Font styles to use
Sans Serif

Requirements
Must have
• - Navigation:
1) Home 2) Auctions 3) Real Estate Listings 4) Our Services 5) Why Auctions 6) About Us 7) Past Auctions 8) Contact Us

Homeage will have slideshow, please use stock real estate image as the initial slide. Homepage will have this content: "Martin Brantow Auctioneer Real Estate Broker

Buying or selling you can count on Martin Brantow Auctioneer to deliver a quality auction experience. We handle all the details from initial handshake to final payment. We are with you every step of the way giving our sellers the service and results they deserve. You only have one chance for a successful auction. Contact us today to see how our experience and know-how can work for you. We are confident that you will appreciate our higher standard of service."

Footer will have smaller company logo, and attached association logos and this contact info:
Phone: (270) 555-0148
Contacts: Martin Brantow
Email: martinbrantow@mailvex.example
Address: 482 Wexcombe Lane • Bowling Green, KY 42190

Widgets:
1) email sign up 2) Social media (twitter, Youtube - can also be in header 3) News & Events Blog widget 4) testimonials blog 5) Featured Video widget
Nice to have
• Nice to Have:
- demonstrate the drop-down menu styling, e.g. under Auctions
-Upcoming Auctions
-Online Auctions
-Past Auctions

```html
<!DOCTYPE html>
<html lang="en">
<head>
<meta charset="utf-8">
<title>Martin Brantow Auctioneer</title>
<link href="https://fonts.googleapis.com/css2?family=Open+Sans:wght@400;600;700&family=Rokkitt:wght@400;500&display=swap" rel="stylesheet">
<style>
:root{
  --blue:#1e9ce0;
  --blue-dark:#1585c4;
  --ink:#3d3d3d;
  --muted:#8a8a8a;
  --line:#e3e3e3;
  --panel:#f3f3f3;
  --topbar:#f4f4f4;
  --footer:#4a4a4a;
  --footer-line:#5c5c5c;
  --footer-text:#cfcfcf;
  --white:#ffffff;
}
*{margin:0;padding:0;box-sizing:border-box}
html,body{width:673px;height:1200px;overflow:hidden}
body{position:relative;background:var(--white);font-family:"Open Sans",Arial,sans-serif;color:var(--ink)}
.abs{position:absolute}
.serif{font-family:"Rokkitt",Georgia,serif}

/* top bar */
.topbar{left:0;top:0;width:673px;height:25px;background:var(--topbar);font-size:6px;color:var(--muted)}
.topbar .lang{left:48px;top:9px}
.topbar .phone{left:96px;top:9px}
.topbar .social{right:56px;top:8px;display:flex;gap:12px}
.topbar .social span{width:7px;height:7px;border-radius:50%;background:#b9b9b9;display:block}

/* header */
.header{left:0;top:25px;width:673px;height:48px;background:var(--white);box-shadow:0 1px 2px rgba(0,0,0,.08);z-index:2}
.brand{left:45px;top:6px;display:flex;align-items:center;gap:5px}
.brand .mark{width:12px;height:12px;background:var(--blue)}
.brand .name{font-size:10px;font-weight:700;color:var(--blue-dark);line-height:1.05;width:60px}
.nav{right:48px;top:0;height:48px;display:flex;align-items:center;font-size:7px;color:#555}
.nav a{color:inherit;text-decoration:none;margin-left:11px}
.nav .active{color:var(--blue);font-weight:600;border-bottom:1px solid var(--blue);padding-bottom:1px}

/* hero */
.hero{left:0;top:73px;width:673px;height:232px;background:linear-gradient(180deg,#ececec 0%,#d9d9d9 45%,#c9c4c0 100%)}
.hero-banner{left:49px;top:136px;width:292px;height:60px;background:var(--blue);color:#fff;padding:12px 0 0 8px}
.hero-banner h1{font-family:"Rokkitt",Georgia,serif;font-weight:500;font-size:19px;line-height:1;letter-spacing:-.2px}
.hero-banner p{font-family:"Rokkitt",Georgia,serif;font-size:12.5px;margin-top:4px}
.search{top:204px;width:274px;height:78px;background:#fff;padding:8px 0 0 11px;box-shadow:0 1px 3px rgba(0,0,0,.1)}
.search h2{font-family:"Rokkitt",Georgia,serif;font-weight:400;font-size:16px;color:#444}
.search .field{position:absolute;left:11px;top:33px;width:225px;height:20px;border:1px solid #ddd;font-size:6px;color:#aaa;padding:6px 5px}
.search .go{position:absolute;left:241px;top:33px;width:25px;height:21px;background:var(--blue)}
.search .go svg{position:absolute;left:6px;top:5px}
.search .opts{position:absolute;left:11px;top:61px;font-size:5.5px;color:#777;display:flex;align-items:center;gap:4px}
.search .opts span.sel{border:1px solid #ddd;padding:1px 14px 1px 3px}
.search .note{position:absolute;left:11px;top:62px;font-size:5.5px;color:#777}

/* intro */
.intro-title{left:0;top:346px;width:673px;text-align:center;font-size:16.5px;color:#444}
.intro-text{left:46px;top:377px;width:581px;text-align:center;font-size:6.8px;line-height:13px;color:#9a9a9a}

/* feature cards */
.card{top:457px;width:134px;height:140px;background:var(--panel)}
.card .head{height:35px;display:flex;align-items:center;justify-content:center;gap:5px;font-size:8px;font-weight:600;color:#555}
.card .head i{width:10px;height:10px;border:1.4px solid #5a8fb8;display:block;border-radius:2px}
.card .photo{height:65px}
.card p{font-size:6.8px;line-height:10px;color:#777;padding:9px 8px 0 9px}

/* auctions */
.section-h{font-size:15.5px;color:#444}
.dotted{height:9px;background:repeating-linear-gradient(0deg,#e2e2e2 0 1px,transparent 1px 2px)}
.lot{top:683px;width:189px;height:202px;background:var(--panel)}
.lot .badge{position:absolute;left:7px;top:0;width:31px;height:34px;z-index:2}
.lot .date{position:absolute;left:7px;top:34px;width:31px;height:14px;background:#444;color:#fff;font-family:"Rokkitt",Georgia,serif;font-size:7px;text-align:center;line-height:14px;z-index:2}
.lot .title{position:absolute;left:40px;top:6px;font-family:"Rokkitt",Georgia,serif;font-size:8.4px;line-height:9.5px;color:#444;width:145px}
.lot .photo{position:absolute;left:0;top:27px;width:189px;height:98px}
.lot .meta{position:absolute;left:7px;top:134px;font-size:5.8px;line-height:11px;color:#555}
.lot .actions{position:absolute;left:0;top:164px;width:189px;height:20px;border-top:1px solid #fff;display:flex;align-items:center;font-size:5.8px;color:var(--blue)}
.lot .actions span{padding-left:9px}
.lot .actions span+span{padding-left:22px}
.lot .price{margin-left:auto;padding:0 10px;font-size:9px;font-weight:700}

.upcoming{left:458px;top:689px;width:164px;height:186px;background:#ececec;padding:7px}
.upcoming .list{background:#fff;height:172px;padding:0 5px}
.event{height:53.5px;position:relative;border-bottom:1px solid #eee}
.event .thumb{position:absolute;left:0;top:5px;width:50px;height:34px}
.event h4{position:absolute;left:58px;top:6px;font-size:7.2px;font-weight:400;color:#666;letter-spacing:.2px}
.event p{position:absolute;left:58px;top:17px;font-size:5.6px;line-height:7px;color:#777;width:90px}
.event .when{position:absolute;left:0;top:40px;font-size:7px;color:var(--blue);white-space:nowrap}

/* clients */
.clients-band{left:255px;top:906px;width:162px;height:25px;background:var(--blue);color:#fff;text-align:center;font-size:15px;line-height:25px}
.clients{left:60px;top:952px;width:556px;display:flex;justify-content:space-between;align-items:center}
.client{display:flex;align-items:center;gap:5px;font-size:8.5px;font-weight:700;color:#444}
.client i{width:14px;height:14px;border-radius:50%;background:#444;display:block}

/* footer */
.footer{left:0;top:1005px;width:673px;height:195px;background:var(--footer);color:var(--footer-text)}
.fcol{top:26px;width:124px}
.fcol h3{font-size:9px;font-weight:600;color:#eee}
.stripe{height:2px;width:122px;margin-top:8px;background:linear-gradient(90deg,#1e9ce0 0 20%,#e67e22 20% 40%,#9b59b6 40% 60%,#e74c6b 60% 80%,#1e9ce0 80%)}
.fdiv{top:20px;width:1px;height:146px;background:var(--footer-line)}
.news{display:flex;gap:6px;margin-top:14px;width:128px}
.news .thumb{width:26px;height:26px;flex:none}
.news .txt{flex:1;font-size:6px;line-height:8.4px;color:#ddd}
.news .txt small{display:flex;justify-content:space-between;font-size:5.4px;color:#aaa;margin-top:2px;width:100%}
.viewall{font-size:5.6px;color:#ddd;text-decoration:underline;margin-top:5px}
.quote{display:flex;gap:5px;margin-top:12px;font-size:5.8px;line-height:9.6px;color:#ccc}
.quote i{width:6px;height:6px;border-radius:50%;background:var(--blue);flex:none;margin-top:2px}
.quote b{color:var(--blue);font-weight:400}
.quote em{color:#e6a23c;font-style:normal}
.flabel{font-size:6.5px;color:#aaa;margin-top:16px}
.email{margin-top:7px;width:118px;height:20px;border:1px solid #888;display:flex;font-size:5.8px;color:#aaa}
.email span{flex:1;padding:6px 5px}
.email b{width:21px;border-left:1px solid #888}
.socials{display:flex;gap:8px;margin-top:7px}
.socials i{width:16px;height:16px;border:1px solid #999;border-radius:50%;display:block}
.contact{display:flex;gap:8px;margin-top:13px;font-size:6.5px;line-height:13px;color:#ddd}
.contact svg{flex:none;margin-top:2px}
.fbottom{left:62px;top:1170px;width:552px;border-top:1px solid var(--footer-line);padding-top:8px;display:flex;font-size:6px;color:#ccc}
.fbottom .right{margin-left:auto}
</style>
</head>
<body>

<div class="abs topbar">
  <span class="abs lang">English ▾</span>
  <span class="abs phone">✆ (270) 555-0148</span>
  <div class="abs social"><span></span><span></span><span></span><span></span></div>
</div>

<header class="abs header">
  <div class="abs brand"><span class="mark"></span><span class="name">Martin Brantow</span></div>
  <nav class="abs nav">
    <a class="active">Home</a><a>Auctions</a><a>Real Estate Listings</a><a>Our Services</a><a>Why Auctions</a><a>About Us</a><a>Past Auctions</a><a>Contact Us</a>
  </nav>
</header>

<section class="abs hero" role="img" aria-label="Bright modern living room with white sofa and fur throws"></section>
<div class="abs hero-banner">
  <h1>Welcome To The Martin Brantow</h1>
  <p>Auctioneer Real Estate Broker</p>
</div>

<form class="abs search" style="left:49px">
  <h2>Buy A Home</h2>
  <div class="field">City Zip , Address , School Or Mls</div>
  <div class="go"><svg width="12" height="12" viewBox="0 0 12 12"><circle cx="5" cy="5" r="3.6" fill="none" stroke="#fff" stroke-width="1.8"/><path d="M7.6 7.6L11 11" stroke="#fff" stroke-width="2"/></svg></div>
  <div class="opts">Price <span class="sel">No Min</span> To <span class="sel">No Max</span>&nbsp;&nbsp;&nbsp; Beds <span class="sel">No Min</span> Baths <span class="sel">No Max</span></div>
</form>
<form class="abs search" style="left:347px">
  <h2>Sell My Home</h2>
  <div class="field">123 Main Street Hometown , Wa</div>
  <div class="go"><svg width="12" height="12" viewBox="0 0 12 12"><circle cx="5" cy="5" r="3.6" fill="none" stroke="#fff" stroke-width="1.8"/><path d="M7.6 7.6L11 11" stroke="#fff" stroke-width="2"/></svg></div>
  <div class="note">Get a no-obligation consultation on your home's market value.</div>
</form>

<h2 class="abs intro-title serif" style="font-weight:400">We Are Providing Best Real Estate Deals</h2>
<p class="abs intro-text">Buying or selling you can count on Martin Brantow Auctioneer to deliver a quality auction experience. We handle all the details from initial handshake to final payment. We are with you every step of the way giving our sellers the service and results they deserve. You only have one chance for a successful auction. Contact us today to see how our experience and know-how can work for you. We are confident that you will appreciate our higher standard of service."</p>

<div class="abs card" style="left:54px"><div class="head"><i></i>Buy A Home</div><div class="photo" role="img" aria-label="Couple in front of a sold sign" style="background:linear-gradient(135deg,#9bb58a,#c9443d)"></div><p>Find Your Customer Want Buy Home</p></div>
<div class="abs card" style="left:197px"><div class="head"><i></i>Search Home</div><div class="photo" role="img" aria-label="Woman browsing homes on a laptop" style="background:linear-gradient(135deg,#ede9e4,#cfc6bd)"></div><p>Looking to buy your new dream home?</p></div>
<div class="abs card" style="left:341px"><div class="head"><i></i>List Property</div><div class="photo" role="img" aria-label="Woman holding a blank sign" style="background:linear-gradient(90deg,#d8c8b4,#a88a74)"></div><p>Want to list your own property?</p></div>
<div class="abs card" style="left:484px"><div class="head"><i></i>Find Realtor</div><div class="photo" role="img" aria-label="Realtor on the phone at a desk" style="background:linear-gradient(135deg,#e4e4e4,#b8b8b8)"></div><p>Find a Realtor that suits your needs.</p></div>

<h2 class="abs section-h serif" style="left:55px;top:634px;font-weight:400">Online Auctions</h2>
<h2 class="abs section-h serif" style="left:458px;top:632px;font-weight:400">Upcoming Auctions</h2>
<div class="abs dotted" style="left:55px;top:654px;width:563px"></div>

<article class="abs lot" style="left:56px">
  <svg class="badge" viewBox="0 0 31 34"><path d="M15.5 0L31 10V34H0V10Z" fill="#1e9ce0"/><text x="15.5" y="27" text-anchor="middle" font-family="Open Sans,sans-serif" font-size="11" fill="#fff">28</text></svg>
  <div class="date">Start Jan</div>
  <div class="title">Real Estate, Household, Woodworking Equip, Tools</div>
  <div class="photo" role="img" aria-label="Agents handing keys to a couple" style="background:linear-gradient(135deg,#b9c3cc,#6c7784)"></div>
  <div class="meta">Hollis &amp; Varnum Auctioneers LLC &nbsp;2208 Orchard Road<br>Brookvale, PA -- Sat May 31 - 08:30AM</div>
  <div class="actions"><span>View Properties</span><span>Contact Agent</span><span class="price">$ 4567</span></div>
</article>
<article class="abs lot" style="left:254px">
  <svg class="badge" viewBox="0 0 31 34"><path d="M15.5 0L31 10V34H0V10Z" fill="#1e9ce0"/><text x="15.5" y="27" text-anchor="middle" font-family="Open Sans,sans-serif" font-size="11" fill="#fff">28</text></svg>
  <div class="date">Start Jan</div>
  <div class="title">Real Estate, Household, Woodworking Equip, Tools</div>
  <div class="photo" role="img" aria-label="Agent handing house keys to a couple" style="background:linear-gradient(135deg,#c4c8cc,#707880)"></div>
  <div class="meta">Hollis &amp; Varnum Auctioneers LLC &nbsp;2208 Orchard Road<br>Brookvale, PA -- Sat May 31 - 08:30AM</div>
  <div class="actions"><span>View Properties</span><span>Contact Agent</span><span class="price">$ 4567</span></div>
</article>

<aside class="abs upcoming">
  <div class="list">
    <div class="event"><div class="thumb" role="img" aria-label="Barn building on a lawn" style="background:linear-gradient(180deg,#c9cfd4,#7d9a5a)"></div><h4>PUBLIC AUCTION</h4><p>Quillford's Auction Service 27 E. Main St.</p><span class="when">Dunmere, Pa -- Sat May 31 - 09:00AM</span></div>
    <div class="event"><div class="thumb" role="img" aria-label="Barn building on a lawn" style="background:linear-gradient(180deg,#c9cfd4,#7d9a5a)"></div><h4>PUBLIC AUCTION</h4><p>Quillford's Auction Service 27 E. Main St.</p><span class="when">Dunmere, Pa -- Sat May 31 - 09:00AM</span></div>
    <div class="event" style="border:0"><div class="thumb" role="img" aria-label="Barn building on a lawn" style="background:linear-gradient(180deg,#c9cfd4,#7d9a5a)"></div><h4>PUBLIC AUCTION</h4><p>Quillford's Auction Service 27 E. Main St.</p><span class="when">Dunmere, Pa -- Sat May 31 - 09:00AM</span></div>
  </div>
</aside>

<div class="abs dotted" style="left:55px;top:914px;width:563px"></div>
<h2 class="abs clients-band serif" style="font-weight:500">Our Clients</h2>
<div class="abs clients">
  <span class="client"><i></i>CORWIN PSYCH</span>
  <span class="client">HireNest</span>
  <span class="client">LUMET</span>
  <span class="client"><i></i>Veltra Pharma</span>
  <span class="client"><i></i>Marlow Hayes</span>
</div>

<footer class="abs footer">
  <div class="abs fcol" style="left:62px;width:132px">
    <h3>News &amp; Events</h3><div class="stripe"></div>
    <div class="news"><div class="thumb" role="img" aria-label="Business people" style="background:linear-gradient(135deg,#d9d3cc,#7f7a74)"></div><div class="txt">Lorem ipsum dolor &nbsp;amettur sadipscing elitr<small><span>about a day ago</span><span>$12362512</span></small></div></div>
    <div class="news"><div class="thumb" role="img" aria-label="Beach scene" style="background:linear-gradient(135deg,#8fd0e8,#d8c9a4)"></div><div class="txt">Lorem ipsum dolor &nbsp;amettur sadipscing elitr<small><span>about a day ago</span><span>$12362512</span></small></div></div>
    <div class="viewall">View All</div>
  </div>
  <div class="abs fdiv" style="left:199px"></div>
  <div class="abs fcol" style="left:209px;width:130px">
    <h3>Our Clients Says</h3><div class="stripe"></div>
    <div class="quote"><i></i><span><b>@Lorem Ipsum</b> is simply dummy text of the printing and typesetting industry. Lorem Ipsum has <b>been the industr</b><em>y's</em> about month ago</span></div>
    <div class="quote" style="margin-top:6px"><i></i><span><b>@Lorem Ipsum</b> is simply dummy text of the printing and typesetting industry. Lorem Ipsum has <b>been the industr</b><em>y's</em> about month ago</span></div>
  </div>
  <div class="abs fdiv" style="left:347px"></div>
  <div class="abs fcol" style="left:357px">
    <h3>Get In Touch</h3><div class="stripe"></div>
    <div class="flabel" style="margin-top:13px">News Letter</div>
    <div class="email"><span>Email......</span><b></b></div>
    <div class="flabel" style="margin-top:12px">Let Get Social</div>
    <div class="socials"><i></i><i></i><i></i><i></i><i></i></div>
  </div>
  <div class="abs fdiv" style="left:491px"></div>
  <div class="abs fcol" style="left:501px">
    <h3>Contact Us</h3><div class="stripe"></div>
    <div class="contact"><svg width="7" height="8" viewBox="0 0 7 8"><path d="M1 0.5L2.6 0.5 3 2.5 2 3.2Q2.8 5 4.2 5.8L5 4.8 7 5.4 7 7Q3 7.5 1 3Z" fill="#1e9ce0"/></svg><span>(270) 555-0148</span></div>
    <div class="contact" style="margin-top:6px"><svg width="8" height="7" viewBox="0 0 8 7"><rect x=".5" y="1" width="7" height="5.5" fill="none" stroke="#1e9ce0"/><path d="M.5 1L4 4 7.5 1" fill="none" stroke="#1e9ce0"/></svg><span style="font-size:6px">martinbrantow@mailvex.example</span></div>
    <div class="contact" style="margin-top:6px"><svg width="7" height="10" viewBox="0 0 7 10"><path d="M3.5 10L0.6 4.6A3.3 3.3 0 1 1 6.4 4.6Z" fill="#1e9ce0"/><circle cx="3.5" cy="3.4" r="1.2" fill="#4a4a4a"/></svg><span>482 Wexcombe Lane • Bowling<br>Green, KY 42190</span></div>
  </div>
</footer>
<div class="abs fbottom"><span>Terms of Service &nbsp;&nbsp;&nbsp;&nbsp;|&nbsp;&nbsp;&nbsp;&nbsp; Privacy Policy</span><span class="right">© 2014 real estate All Rights Reserved.</span></div>

</body>
</html>
```